Marlowvex Website Concept

We would like a one page website. Please refer to the attached files for more information.

Please reference file attachment version 1.1.

```html
<!DOCTYPE html>
<html lang="en">
<head>
<meta charset="utf-8">
<title>Marlowvex</title>
<link href="https://fonts.googleapis.com/css2?family=Open+Sans:wght@400;600&family=Cinzel:wght@500&display=swap" rel="stylesheet">
<style>
:root{
  --brand:#4ec2e7;
  --brand-dark:#2a9fcb;
  --ink:#444;
  --muted:#8c8c8c;
  --line:#e6e6e6;
  --panel:#f4f4f4;
  --footer:#3a3a3a;
  --logo:#4a5a72;
}
*{box-sizing:border-box;margin:0;padding:0}
html,body{width:863px;height:1200px;overflow:hidden;background:#fff}
body{position:relative;font-family:"Open Sans",Arial,sans-serif;color:var(--ink)}
.abs{position:absolute}
.logo{left:40px;top:31px;display:flex;align-items:center;gap:8px}
.logo-dot{width:36px;height:36px;border-radius:50%;background:var(--logo)}
.logo-name{font-family:"Cinzel",serif;font-weight:500;font-size:24px;color:var(--logo);letter-spacing:.5px}
.phone{right:40px;top:44px;display:flex;align-items:center;gap:8px;color:var(--brand-dark);font-size:14px}
.nav{left:40px;top:112px;width:783px;height:49px;background:var(--brand);display:flex;border-radius:2px;overflow:hidden}
.nav a{color:#fff;text-decoration:none;font-size:13.5px;display:flex;align-items:center;justify-content:center;border-right:1px solid #62cbee}
.nav a.active{background:#111;border:none}
.hero{left:40px;top:173px;width:783px;height:345px;border-radius:4px;background:radial-gradient(ellipse at 50% 45%,#f6e4e4 0%,#e9d6d2 25%,#d7b39f 50%,#eceef3 75%,#f5f6f8 100%)}
.arrow{top:329px;width:33px;height:33px}
.welcome{left:40px;top:536px;font-size:20px;font-weight:400;color:#555}
.welcome span{color:var(--brand-dark);font-size:24px}
.rule{left:40px;top:579px;width:504px;height:1px;background:var(--line)}
.photo{left:40px;top:599px;width:173px;height:241px;background:linear-gradient(160deg,#4d5a3e,#7a6a55 45%,#e9b7bd 70%,#6b4a34)}
.about{left:229px;top:594px;width:315px;font-size:10px;line-height:18px;color:var(--muted);text-align:justify}
.about p+p{margin-top:16px}
.btn{background:var(--brand);color:#fff;border-radius:3px;font-size:12px;display:flex;align-items:center;justify-content:center}
.read{left:229px;top:810px;width:85px;height:31px}
.quote{left:561px;top:547px;width:262px;height:295px;background:var(--panel)}
.quote-head{height:43px;border-bottom:1px solid #e8e8e8;display:flex;align-items:center}
.quote-icon{width:43px;height:43px;border-right:1px solid #e8e8e8;display:flex;align-items:center;justify-content:center}
.quote-head h2{font-weight:400;font-size:19px;color:#777;margin-left:14px}
.field{position:absolute;left:21px;width:221px;height:34px;background:#fff;border:1px solid #e3e3e3;border-radius:3px;font-size:12px;color:#999;padding:0 12px;display:flex;align-items:center}
.submit{left:21px;top:249px;width:72px;height:28px;font-size:14px;font-weight:600;border-radius:2px}
.card{top:882px;width:184px;height:205px;border:1px solid #eee;background:#fff}
.card-img{height:138px}
.card-title{height:67px;display:flex;align-items:center;justify-content:center;text-align:center;font-size:14px;line-height:18px;color:#8a8a8a;padding:0 10px}
.footer{left:40px;top:1118px;width:783px;height:52px;background:var(--footer);display:flex;align-items:center;justify-content:space-between;padding:0 17px;font-size:10px;color:#aaa}
.social{display:flex;gap:5px}
.social span{width:26px;height:26px;border:1.5px solid #777;border-radius:50%}
.foot-links a{color:#aaa;text-decoration:none}
.foot-links i{font-style:normal;margin:0 6px}
</style>
</head>
<body>
<div class="abs logo"><div class="logo-dot"></div><div class="logo-name">MARLOWVEX</div></div>
<div class="abs phone">
  <svg width="28" height="24" viewBox="0 0 28 24"><circle cx="16" cy="11" r="10" fill="none" stroke="#666" stroke-width="1.6"/><text x="16" y="14.5" font-size="9" font-family="Open Sans" text-anchor="middle" fill="#666" font-weight="600">24</text><path d="M3 8c-2 5 1 11 7 14l2-3-3-2-2 1c-1-2-2-4-1-6l2-1-1-3z" fill="#666"/></svg>
  <span>Call : (020) 555 0148</span>
</div>
<nav class="abs nav">
  <a class="active" style="width:76px">Home</a>
  <a style="width:142px">About marlowvex</a>
  <a style="width:93px">Services</a>
  <a style="width:138px">Request a Quote</a>
  <a style="width:87px">Careers</a>
  <a style="width:147px">Contact Marlowvex</a>
</nav>
<div class="abs hero" role="img" aria-label="Hands holding a pink piggy bank"></div>
<svg class="abs arrow" style="left:60px" viewBox="0 0 33 33"><circle cx="16.5" cy="16.5" r="15.5" fill="none" stroke="#5aa9c9" stroke-width="1.6"/><path d="M19 10l-6 6.5 6 6.5" fill="none" stroke="#5aa9c9" stroke-width="1.8"/></svg>
<svg class="abs arrow" style="left:771px" viewBox="0 0 33 33"><circle cx="16.5" cy="16.5" r="15.5" fill="none" stroke="#5aa9c9" stroke-width="1.6"/><path d="M14 10l6 6.5-6 6.5" fill="none" stroke="#5aa9c9" stroke-width="1.8"/></svg>

<h1 class="abs welcome">Welcome To <span>Marlowvex</span></h1>
<div class="abs rule"></div>
<div class="abs photo" role="img" aria-label="Smiling girl holding a piggy bank"></div>
<div class="abs about">
  <p>Marlowvex is a United States-based tier one security firm specializing in the protection of financial services professionals, executives and their families. We manage engagements resulting from general and specific threats throughout the United States and abroad on behalf of our domestic clients.</p>
  <p>We deliver our services exclusively through associates and contractors with United States special operations, secret service, federal intelligence, or equivalent experience and training. We are one of only a handful of domestic security firms that offers scalable, tier one security services in every market in the United States.</p>
</div>
<div class="abs btn read">Read More</div>

<aside class="abs quote">
  <div class="quote-head">
    <div class="quote-icon"><svg width="20" height="15" viewBox="0 0 20 15"><rect x="1" y="1" width="18" height="13" fill="none" stroke="#3bb3e0" stroke-width="1.4"/><path d="M1 1l9 7 9-7M1 14l6-6M19 14l-6-6" fill="none" stroke="#3bb3e0" stroke-width="1.4"/></svg></div>
    <h2>Get A Quote</h2>
  </div>
  <div class="field" style="top:62px">Name *</div>
  <div class="field" style="top:107px">Address *</div>
  <div class="field" style="top:152px">Email *</div>
  <div class="field" style="top:199px">Phone *</div>
  <div class="abs btn submit">Submit</div>
</aside>

<div class="abs card" style="left:40px"><div class="card-img" role="img" aria-label="Laptop keyboard with a padlock" style="background:linear-gradient(160deg,#222,#777 50%,#ddd)"></div><div class="card-title">Threat Assessment</div></div>
<div class="abs card" style="left:239px"><div class="card-img" role="img" aria-label="Hands protecting a stack of coins" style="background:linear-gradient(160deg,#eee,#c9a3b7 45%,#f3e7e2)"></div><div class="card-title">Threat Avoidance Plan &amp; Dossier Creation</div></div>
<div class="abs card" style="left:439px"><div class="card-img" role="img" aria-label="Businessman holding a glowing globe" style="background:linear-gradient(150deg,#bfe0ec,#7ab4cf 50%,#5a6f86)"></div><div class="card-title">Elite Executive Protection</div></div>
<div class="abs card" style="left:638px"><div class="card-img" role="img" aria-label="Hands reviewing charts on a tablet" style="background:linear-gradient(150deg,#e9eef2,#b9d0e4 50%,#f2efe6)"></div><div class="card-title">Threat Avoidance Plan &amp; Dossier Maintenance</div></div>

<footer class="abs footer">
  <span>©2013 - 2014 marlowvex360, All Rights Reserved.</span>
  <div class="social"><span></span><span></span><span></span><span></span><span></span></div>
  <div class="foot-links"><a>About us</a><i>|</i><a>Services</a><i>|</i><a>Get a quote</a><i>|</i><a>contact</a></div>
</footer>
</body>
</html>
```